TRELUDAX.live*

I am needing a web site built for the main purpose of uploading podcasts
(MP3 files) to be viewed by large audiences of 1000+ site visitors on a regular basis. I have created a rough draft of how I want the site to look.

i have created a rough draft of the home page - the LOGO for this site is a spectacular lightening bolt which appears on my home page sample... the file for this image I purchased is too large to download to your site. I will supply on reuquest.

There will be 5 pages; HOME ABOUT RESOURCES DEVOTIONALS GLENN.
I have all the content prepared for each of the above pages.

Target Market(s)

All people groups seeking positive and encouraging words, life lessons and testimonies of faith.

Coding

Coded - Design and coding required

Number of Pages Required

1 page

Colors
3176b5

Requirements
Must have
• The design and layout provided - my sample

Black backgrounds as shown on my sample

```html
<!DOCTYPE html>
<html lang="en">
<head>
<meta charset="utf-8">
<title>TRELUDAX.live — Glenn</title>
<link href="https://fonts.googleapis.com/css2?family=Playfair+Display:wght@700;900&family=Open+Sans:wght@400&display=swap" rel="stylesheet">
<style>
  :root {
    --ink: #ffffff;
    --page-bg: #000000;
    --hero-deep: #020a2e;
    --hero-mid: #0a2a8a;
    --hero-glow: #3176b5;
    --accent: #1fc8f0;
    --muted-glow: #3a3a40;
    --serif: "Playfair Display", "Bodoni Moda", serif;
    --sans: "Open Sans", Arial, sans-serif;
  }
  * { margin: 0; padding: 0; box-sizing: border-box; }
  html, body { width: 1028px; height: 1200px; overflow: hidden; background: var(--page-bg); }
  .canvas { position: relative; width: 1028px; height: 1200px; background: var(--page-bg); color: var(--ink); overflow: hidden; }

  .hero { position: absolute; left: 0; top: 0; width: 1028px; height: 439px; }
  .hero-art {
    position: absolute; inset: 0;
    background:
      radial-gradient(ellipse 260px 200px at 40% 55%, rgba(31,200,240,.55), transparent 70%),
      radial-gradient(ellipse 180px 160px at 88% 85%, rgba(31,200,240,.45), transparent 70%),
      radial-gradient(ellipse 500px 380px at 35% 35%, var(--hero-mid), transparent 75%),
      linear-gradient(160deg, var(--hero-mid) 0%, var(--hero-deep) 70%, #01040f 100%);
  }

  .site-nav a, .footer-nav a {
    position: absolute; font-family: var(--serif); font-weight: 700;
    color: var(--ink); text-decoration: none; text-transform: uppercase; white-space: nowrap;
    transform: translateX(-50%);
  }
  .site-nav a { top: 44px; font-size: 12.5px; }
  .site-nav a.is-current::after {
    content: ""; position: absolute; left: 50%; bottom: -6px; width: 22px; height: 2px;
    background: var(--accent); transform: translateX(-50%);
  }
  .brand {
    position: absolute; left: 507px; top: 28px; transform: translateX(-50%);
    font-family: var(--serif); font-weight: 900; font-size: 34px; letter-spacing: .5px; white-space: nowrap;
  }
  .hero-title {
    position: absolute; left: 530px; top: 205px; transform: translateX(-50%);
    font-family: var(--serif); font-weight: 700; font-size: 62px; line-height: 1; letter-spacing: -1px;
  }

  .profile-heading {
    position: absolute; left: 557px; top: 520px; transform: translateX(-50%);
    font-family: var(--serif); font-weight: 700; font-size: 30px; letter-spacing: -.5px; white-space: nowrap;
  }
  .profile-photo {
    position: absolute; left: 89px; top: 610px; width: 411px; height: 309px;
    border: 1.5px solid #e8e8e8;
    background: linear-gradient(180deg, #3b3d3a 0%, #5a5c58 45%, #8a8a88 80%, #9d9d9b 100%);
  }
  .profile-bio {
    position: absolute; left: 528px; top: 612px; width: 455px;
    font-family: var(--sans); font-size: 13px; line-height: 16.5px;
  }
  .profile-bio p { margin-bottom: 32px; }

  .footer-glow {
    position: absolute; bottom: 0; width: 170px; height: 200px;
  }
  .footer-glow.left { left: 0; background: radial-gradient(ellipse 120px 150px at 20% 70%, var(--muted-glow), transparent 75%); }
  .footer-glow.right { right: 0; background: radial-gradient(ellipse 120px 150px at 80% 55%, var(--muted-glow), transparent 75%); }

  .social-links { position: absolute; left: 447px; top: 1030px; display: flex; gap: 3px; }
  .social-links span {
    width: 28px; height: 28px; border: 1.3px solid var(--ink); border-radius: 50%; display: block;
  }
  .footer-nav a { top: 1078px; font-size: 13.5px; }
  .copyright {
    position: absolute; left: 514px; top: 1108px; transform: translateX(-50%);
    font-family: var(--sans); font-size: 12px; white-space: nowrap;
  }
</style>
</head>
<body>
<div class="canvas">
  <header class="hero">
    <div class="hero-art" role="img" aria-label="Electric blue lightning bolt artwork on a deep blue background"></div>
    <nav class="site-nav">
      <a href="#" style="left:90px">Home</a>
      <a href="#" style="left:172px">About</a>
      <a href="#" class="is-current" style="left:257px">Glenn</a>
      <a href="#" style="left:773px">Resources</a>
      <a href="#" style="left:895px">Devotionals</a>
    </nav>
    <div class="brand">TRELUDAX.live</div>
    <h1 class="hero-title">GLENN</h1>
  </header>

  <main>
    <h2 class="profile-heading">GLENN MARLOW PASTOR</h2>
    <div class="profile-photo" role="img" aria-label="Black and white photo of Glenn seated on his motorcycle"></div>
    <div class="profile-bio">
      <p>Glenn has been involved in motorcycle ministries and outreach for over fifteen years and since 2011 when he became an ordained pastor, under the Coastal Fellowship Convention he has officiated many weddings, celebration of life services and baby dedications.</p>
      <p>He pastored a biker church in Surrey for five years and has been a part of a number of outreach groups and ministries over the years which have been focused in the biker world demographic.</p>
      <p>He has a passion to reach out to the broken hearted, in particular people suffering from drug and alcohol addiction and over the years has been an advocate for those who are suffering and wanting to break the chains.</p>
      <p>Glenn believes his gifting from God is to be an encourager... His desire is to be real, transparent and to make a positive difference in people’s lives and God’s Kingdom.</p>
    </div>
  </main>

  <footer>
    <div class="footer-glow left" role="img" aria-label="Faint grey lightning decoration"></div>
    <div class="footer-glow right" role="img" aria-label="Faint grey lightning decoration"></div>
    <div class="social-links" aria-label="Social links">
      <span></span><span></span><span></span><span></span>
    </div>
    <nav class="footer-nav">
      <a href="#" style="left:281px">Home</a>
      <a href="#" style="left:372px">About</a>
      <a href="#" style="left:465px">Glenn</a>
      <a href="#" style="left:574px">Resources</a>
      <a href="#" style="left:708px">Devotionals</a>
    </nav>
    <p class="copyright">© 2020 Company Name | All Rights Reserved</p>
  </footer>
</div>
</body>
</html>
```